*** Einladungsdesign für Start-up Event gesucht ***
Zielgruppe
Für eine innovative Start-up Veranstaltung suchen wir ein stylishes, progressives Layout für die Einladungskarten. Die Veranstaltung heißt
#BrightHorizonLab
und soll als schlichter Schriftzug in die Einladungen eingearbeitet sein. Die exakte Schriftart hierfür etc. wird noch übermittelt. Im Gegensatz das restliche Design gerne futuristisch und modern gehalten sein. Dennoch insgesamt hochwertiger Gesamteindruck
Aufgabenstellung
Name: #BrightHorizonLab
Daten: 4 Seiten
Deckblatt.
linke Innenseite: kurzer Text/Grußwort:
YOUNG. CREATIVE. NIGHT.
Das Internet hat die Welt verändert und sich tief in unserer Gesellschaft verankert. Es ist die Chance unserer Generation diese Digitalisierung zu nutzen und die Welt von morgen weiterzuentwickeln
Freuen Sie sich auf eine inspirierende Nacht im Zeichen der „young leading minds of our time“. Ein Podium für Macher von heute und morgen.
FAST. FORWARD. FUTURE.
rechte Innenseite: Einladungstext
Wir freuen uns
_______________________________ (hier wird Name handschriftlich eingetragen)
zur exklusiven #BrightHorizonLab-Night
einladen zu dürfen.
Datum: 01. Februar 2015
Uhrzeit: ab 20:30 Uhr
Ort: xxxxxx, Anfahrt über xxxxxxx
r.s.v.p. bis zum 14. Januar 2014 unter xxxxxxx
Rückseite: Sponsoren & Partner der Veranstaltung
Stehen noch nicht fest, daher bitte einfach mit ca. 5 farbigen Logos (z.B. Vorel AG) arbeiten.
Farbwelt: Gerne an verschiedenen Grautönen, Schwarz und Rot orientieren.
Format: Gängiges Format, 4C (Sonderfarben & Stanzformate können gerne vorgeschlagen werden),
Versand: Print (ca. 200 Stück) & Mail
Mögliche Motive: zB 3D-Formen, grobe Pixel, etc.
Nach Rücksprache kann der Designer auch in die Veranstaltung eingearbeitet werden oder sich vor Ort den Gründern und Wirtschaftsentscheidern präsentieren.

```html
<!DOCTYPE html>
<html lang="de">
<head>
<meta charset="utf-8">
<title>#BrightHorizonLab – Einladung Innenseiten</title>
<link href="https://fonts.googleapis.com/css2?family=Roboto+Slab:wght@300;400&family=Roboto:wght@400&display=swap" rel="stylesheet">
<style>
  :root {
    --bg: #f2f2f2;
    --paper: #ffffff;
    --grey: #c4cbcf;
    --red: #d4124e;
    --ink: #1c1c1c;
    --label: #f4f6f7;
  }
  html, body { margin: 0; padding: 0; }
  body {
    width: 1200px; height: 1108px; overflow: hidden;
    background: var(--bg);
    font-family: "Roboto", Arial, sans-serif;
    color: var(--ink);
    position: relative;
  }
  .spread {
    position: absolute; left: 80px; top: 294px;
    width: 1040px; height: 520px;
    display: flex;
    box-shadow: 0 6px 24px rgba(0,0,0,.12);
  }
  .page { position: relative; width: 520px; height: 520px; background: var(--paper); overflow: hidden; }
  .page--left { border-right: 1px solid #e3e6e8; }
  .headline {
    font-family: "Roboto Slab", Georgia, serif; font-weight: 300;
    color: var(--red); text-transform: uppercase;
    margin: 0; line-height: 1.12; letter-spacing: .5px;
  }
  /* left page */
  .intro-band { position: absolute; left: 0; top: 0; width: 100%; height: 215px; background: var(--grey); }
  .intro-band .headline { position: absolute; left: 48px; top: 70px; font-size: 34px; }
  .intro-text { position: absolute; left: 48px; top: 250px; width: 330px; font-size: 14px; line-height: 1.75; margin: 0; }
  /* right page */
  .greeting { position: absolute; left: 0; top: 0; width: 100%; height: 190px; }
  .greeting .headline { position: absolute; left: 40px; top: 48px; font-size: 30px; }
  .signature-field { position: absolute; left: 232px; top: 52px; width: 170px; height: 44px; }
  .invite-line { position: absolute; left: 232px; top: 108px; margin: 0; font-size: 15px; line-height: 1.4; }
  .details { position: absolute; left: 0; top: 190px; width: 100%; height: 330px; background: var(--grey); }
  .detail { position: absolute; }
  .detail__label { display: block; font-size: 11px; color: var(--label); }
  .detail__value { display: block; font-family: "Roboto Slab", Georgia, serif; font-size: 28px; line-height: 1.1; }
  .detail--date { left: 40px; top: 40px; }
  .detail--time { left: 40px; top: 102px; }
  .detail--place { left: 290px; top: 76px; }
  .detail__note { margin: 4px 0 0; font-size: 10px; line-height: 1.35; color: var(--label); }
</style>
</head>
<body>
  <main class="spread">
    <section class="page page--left">
      <div class="intro-band">
        <h2 class="headline">Fast.<br>Forward.<br>Future.</h2>
      </div>
      <p class="intro-text">Freuen Sie sich auf eine inspirierende Nacht im Zeichen der «young leading minds of our time». Ein Podium für Macher von heute und morgen.</p>
    </section>
    <section class="page page--right">
      <div class="greeting">
        <h1 class="headline">Wir<br>freuen<br>uns</h1>
        <svg class="signature-field" role="img" aria-label="Handschriftlich eingetragener Gästename" viewBox="0 0 170 44">
          <rect width="170" height="44" fill="#eef0f1"/>
        </svg>
        <p class="invite-line">zur exklusiven #BrightHorizonLab-Night<br>einladen zu dürfen.</p>
      </div>
      <div class="details">
        <div class="detail detail--date">
          <span class="detail__label">Datum</span>
          <span class="detail__value">01. Februar 2015</span>
        </div>
        <div class="detail detail--time">
          <span class="detail__label">Uhrzeit</span>
          <span class="detail__value">ab 20:30 Uhr</span>
        </div>
        <div class="detail detail--place">
          <span class="detail__label">Ort</span>
          <span class="detail__value">Musterhausen</span>
          <p class="detail__note">Anfahrt über xxxxxxx<br>r.s.v.p. bis zum 14. Januar 2014<br>unter xxxxxxx</p>
        </div>
      </div>
    </section>
  </main>
</body>
</html>
```